Building Servicess

We need a new business card design for a company. We specialise in: Electrical/Site temporary electrics, Data/Network Installation, Passive Fire Protection

Industry/Entity Type

Construction

Contact Information for Business Card

Services provided as detailed on project description

Font styles to use
Serif

Colors
0054AA
0677BA
7BADD7
CADEEF
E8F1F8
00AB8E
00BBA5
67D7C9
C6EFE9
E9F9F6
EB3D1F
EC4F4E
F09395
F8D3D4
FCEDEE

Requirements
Must have
• Company logo-contact details-phone numbers

```html
<!DOCTYPE html>
<html lang="en">
<head>
<meta charset="utf-8">
<title>Meridian Build Services Ltd – Business Card</title>
<link href="https://fonts.googleapis.com/css2?family=Open+Sans:ital,wght@0,400;0,700;1,400&display=swap" rel="stylesheet">
<style>
  :root {
    --brand-blue: #1474be;
    --ink-grey: #555a5f;
    --stripe-grey: #8c8f93;
    --paper: #ffffff;
    --backdrop: #2b2c2e;
  }
  * { margin: 0; padding: 0; box-sizing: border-box; }
  html, body { width: 1200px; height: 900px; overflow: hidden; }
  body {
    background: var(--backdrop);
    font-family: "Open Sans", Arial, sans-serif;
    position: relative;
  }
  .card {
    position: absolute;
    left: 320px;
    width: 560px;
    height: 320px;
    overflow: hidden;
    box-shadow: 0 10px 30px rgba(0,0,0,.45);
  }
  .card--front { top: 100px; background: var(--paper); }
  .card--back { top: 480px; background: var(--brand-blue); }

  .holder { position: absolute; left: 34px; top: 92px; }
  .holder__name {
    color: var(--brand-blue); font-weight: 700; font-size: 21px;
    letter-spacing: .5px; line-height: 1.1;
  }
  .holder__title { color: var(--ink-grey); font-style: italic; font-size: 13px; margin-top: 2px; }

  .divider {
    position: absolute; left: 30px; right: 40px; top: 150px;
    height: 1px; background: var(--brand-blue);
  }

  .wordmark {
    position: absolute; right: 40px; top: 62px; text-align: right;
    color: var(--brand-blue); font-weight: 700; line-height: 1.15;
    display: flex; align-items: center; gap: 10px;
  }
  .wordmark__square { width: 16px; height: 16px; background: currentColor; flex: none; }
  .wordmark__name { font-size: 22px; letter-spacing: 1px; }
  .card--back .wordmark {
    position: absolute; left: 0; right: 0; top: 0; bottom: 0;
    justify-content: center; color: var(--paper); text-align: center;
  }
  .card--back .wordmark__name { font-size: 32px; letter-spacing: 2px; }
  .card--back .wordmark__square { width: 22px; height: 22px; }

  .contacts { position: absolute; left: 34px; top: 164px; list-style: none; }
  .contacts li {
    display: flex; align-items: center; gap: 8px;
    color: var(--ink-grey); font-size: 13px; line-height: 22px;
  }
  .contacts svg { width: 12px; height: 12px; fill: var(--brand-blue); flex: none; }

  .address {
    position: absolute; right: 40px; top: 168px; text-align: right;
    color: var(--ink-grey); font-size: 13px; line-height: 20px;
  }

  .footer-band { position: absolute; left: 0; bottom: 0; width: 560px; height: 90px; }
  .website {
    position: absolute; right: 40px; bottom: 0; height: 32px;
    display: flex; align-items: center;
    color: var(--paper); font-size: 13px; line-height: 1;
  }
</style>
</head>
<body>

<section class="card card--front">
  <div class="holder">
    <div class="holder__name">TOMAS BRENNAN</div>
    <div class="holder__title">Managing Director</div>
  </div>

  <div class="wordmark">
    <span class="wordmark__square"></span>
    <span class="wordmark__name">MERIDIAN BUILD<br>SERVICES LTD</span>
  </div>

  <div class="divider"></div>

  <ul class="contacts">
    <li>
      <svg viewBox="0 0 24 24"><path d="M6.6 10.8a15 15 0 0 0 6.6 6.6l2.2-2.2a1 1 0 0 1 1-.25 11.4 11.4 0 0 0 3.6.57 1 1 0 0 1 1 1V20a1 1 0 0 1-1 1A17 17 0 0 1 3 4a1 1 0 0 1 1-1h3.5a1 1 0 0 1 1 1c0 1.25.2 2.45.57 3.57a1 1 0 0 1-.25 1z"/></svg>
      020 3946 1870
    </li>
    <li>
      <svg viewBox="0 0 24 24"><path d="M7 1h10a2 2 0 0 1 2 2v18a2 2 0 0 1-2 2H7a2 2 0 0 1-2-2V3a2 2 0 0 1 2-2zm0 3v14h10V4z"/></svg>
      075 0321 4408
    </li>
    <li>
      <svg viewBox="0 0 24 24"><path d="M2 5h20v14H2zm2 2v.5l8 5 8-5V7l-8 5z"/></svg>
      info@meridianbuild.com
    </li>
  </ul>

  <div class="address">1840 Harbor View Drive<br>Bayside CA 90211</div>

  <svg class="footer-band" viewBox="0 0 560 90" aria-hidden="true">
    <path d="M0 6 L0 13 L176 60 L196 60 L196 55 Z" fill="var(--stripe-grey)"/>
    <path d="M0 20 L170 64 Q190 58 215 58 L560 58 L560 90 L0 90 Z" fill="var(--brand-blue)"/>
  </svg>
  <div class="website">www.meridianbuild.com</div>
</section>

<section class="card card--back">
  <div class="wordmark">
    <span class="wordmark__square"></span>
    <span class="wordmark__name">MERIDIAN BUILD<br>SERVICES LTD</span>
  </div>
</section>

</body>
</html>
```